GlimmerFrocks.com Banner AD

We are looking for some talented creators to create for us a banner ad for our online clothing store that specializes in dresses. We are looking for a fresh, clean, and sleek LUMA, P&Q, and Plume appeal- clean, modern and sophisticated.

We would like for the final project to appear professionally done, we've had projects completed by several talent out there that did not capture our image, and let's just say it was too cluttered and appeared as if a high school editor had completed it.

I have attached a few files for you to reference, I have File 1, 2, 3, 8 and the P&Q photos as examples of what we DO like.

I have attached File 5, which is the work of one the designers that was working on this project. Although it is very simple and gets the point across, it doesn't come across like a magazine editorial.

I have attached File 6, that is the main photo we wish to use for our banner.

I have attached File 7, which is what a creator had done for us via Taskfern.com, that is a good example of what we do NOT want.

That is about sums it up! I hope the examples are useful tools for you!
Updates

Hi Designers!

Thank you so much for your submissions! I enjoy viewing each and every one of them! Please view my update on what I am looking for, I have made some adjustments and have added a few more examples to reference, I have made my direction a bit more clearer. Because it seems some designers are not quite understanding my direction. I know you all have amazing talent and I am hoping to see something I am looking for and I love soon! If you have any other questions, please don't hesitate to ask! 

Target Market(s)

Our company targets women of all ages, we carry dresses that cater to every occasion, whether its an older woman looking for a dress to attend a wedding or a teenager looking for a prom dress. We want our front page banner to appear fresh, clean, with a feminine touch, we want to stray from tacky (gradients, etc..) and keep it classy all while maintaining that magazine editorial element, we want to be more fashion focused, like Plume. We want this project to appear professionally done. Our desired concept is something out of a magazine editorial, not too much going on, while shifting focus more on the dress itself than a design element like flowers or spring backgrounds.

Industry/Entity Type

High School

Requirements
Must have
• We want a plume fashion appeal, magazine editorial type of look. The phrases below should be included"

"New Season New Sexy Dresses"

"Free U.S shipping on orders $75+"
"Shop our sales up to 60% off"

All of the other phrases do not need to be included. Also, Do not include the parenthesis.
Should not have
• Only include the photo I've attached that appears solo. Please do not include the other 3 dresses that is displayed in a banner that was created for us by another designer. (that is provided as an example only)

```html
<!DOCTYPE html>
<html lang="en">
<head>
<meta charset="utf-8">
<title>GlimmerFrocks.com Spring Banner</title>
<link href="https://fonts.googleapis.com/css2?family=Pacifico&family=Dosis:wght@600;700&family=Oswald:wght@400;500&display=swap" rel="stylesheet">
<style>
  :root {
    --violet: #4a469f;
    --violet-deep: #2f2b7a;
    --violet-veil: rgba(66, 62, 168, 0.9);
    --paper: #ffffff;
    --heart-tint: #f1f2f7;
    --photo-top: #efe4de;
    --photo-mid: #e6cfd6;
    --photo-low: #cbc3e2;
  }
  html, body {
    margin: 0;
    padding: 0;
    overflow: hidden;
    background: var(--paper);
  }
  .banner {
    position: relative;
    width: 1200px;
    height: 1043px;
    overflow: hidden;
    background: var(--paper);
  }
  .heart-decor {
    position: absolute;
    left: 0;
    top: 370px;
    width: 280px;
    height: 280px;
    background: var(--heart-tint);
    border-radius: 0 140px 140px 0;
    opacity: 0.7;
  }
  .model-photo {
    position: absolute;
    left: 770px;
    top: 40px;
    width: 430px;
    height: 1003px;
    background: linear-gradient(180deg, var(--photo-top) 0%, var(--photo-mid) 50%, var(--photo-low) 100%);
    border-radius: 200px 200px 0 0;
  }
  .diagonal-panel {
    position: absolute;
    left: 0;
    top: 0;
    width: 1200px;
    height: 1043px;
  }
  .headline {
    position: absolute;
    left: 36px;
    top: 70px;
    width: 735px;
    height: 108px;
  }
  .headline svg {
    position: absolute;
    inset: 0;
  }
  .headline-text {
    position: absolute;
    left: 0;
    top: 0;
    width: 100%;
    margin: 0;
    text-align: center;
    font-family: "Pacifico", cursive;
    font-weight: 400;
    font-size: 72px;
    line-height: 100px;
    color: var(--paper);
  }
  .subheadline {
    position: absolute;
    left: 40px;
    top: 184px;
    width: 720px;
    margin: 0;
    text-align: center;
    font-family: "Pacifico", cursive;
    font-weight: 400;
    font-size: 47px;
    line-height: 76px;
    color: var(--violet);
  }
  .cta {
    position: absolute;
    left: 100px;
    top: 598px;
    width: 529px;
    height: 107px;
    background: var(--violet);
    border-radius: 8px;
    display: flex;
    align-items: center;
    justify-content: center;
    gap: 28px;
    color: var(--paper);
    font-family: "Dosis", sans-serif;
    font-weight: 700;
    font-size: 38px;
    letter-spacing: 2px;
    text-decoration: none;
  }
  .cta-offer {
    position: absolute;
    left: 100px;
    top: 712px;
    width: 529px;
    margin: 0;
    text-align: center;
    font-family: "Oswald", sans-serif;
    font-weight: 400;
    font-size: 38px;
    line-height: 60px;
    color: var(--violet);
  }
  .shipping-badge {
    position: absolute;
    left: 0;
    top: 905px;
    width: 416px;
    height: 138px;
    background: var(--violet-deep);
    border-radius: 0 22px 0 0;
    box-sizing: border-box;
    padding: 10px 0 0 18px;
    color: var(--paper);
    font-family: "Oswald", sans-serif;
    font-weight: 400;
    font-size: 46px;
    line-height: 56px;
    text-transform: uppercase;
  }
  .shipping-badge p {
    margin: 0;
  }
</style>
</head>
<body>
<main class="banner">
  <div class="heart-decor" role="img" aria-label="Faint decorative heart outline"></div>

  <div class="model-photo" role="img" aria-label="Photo of a smiling woman with long wavy hair wearing a fitted sleeveless watercolor-print dress in pink and purple"></div>

  <svg class="diagonal-panel" viewBox="0 0 1200 1043" aria-hidden="true">
    <polygon points="1200,286 634,1043 1200,1043" fill="var(--violet-veil)"/>
  </svg>

  <header class="headline">
    <svg viewBox="0 0 735 108" width="735" height="108" aria-hidden="true">
      <polygon points="14,8 735,0 722,98 0,108" fill="var(--violet)"/>
    </svg>
    <h1 class="headline-text">Spring has Sprung!</h1>
  </header>

  <p class="subheadline">New Season, New Sexy Dresses!</p>

  <a class="cta" href="#sale">
    <span>SHOP OUR SALES</span>
    <svg width="22" height="30" viewBox="0 0 22 30" aria-hidden="true">
      <polyline points="5,4 16,15 5,26" fill="none" stroke="var(--paper)" stroke-width="5" stroke-linecap="round" stroke-linejoin="round"/>
    </svg>
  </a>
  <p class="cta-offer">UP TO 60% OFF!</p>

  <aside class="shipping-badge">
    <p>Free U.S Shipping</p>
    <p>On orders over $75</p>
  </aside>
</main>
</body>
</html>
```